Lumen UI Style Web Application Design

Our organisation are currently building a new cloud based digital asset management web application. The application will allow users to upload many images, videos, and other media types and manage them in the cloud.
Our typical clients are mid-large sized enterprises (usually with more than 250 employees), but our typical users are marketing teams, graphics designers, web designers and press contacts. The design provided should be tailored to our users, not necessarily the enterprise they work for.
We are looking for a designer to come up with the design for a few key pages within the site based loosely around the Lumen UI Style created for Quillon Phone and Quillon 8. Some examples of Lumen UI in action can be found here:
http://www.sparkmyideas.example/10-designs-inspired-by-veltronics-lumen-ui/
We particularly like the cleanliness of the design and the focus on typography. The Quillon 8 "homepage" also encapsulates the Lumen Ui concepts nicely, and we're sure you will have seen many other examples. Check out the Quillon 8 Tile Shop to see many real world use cases for the designs.
The pages that we would like to see in the design are as follows:
1. The homepage
The homepage of our software is what will be seen by the client once they have logged into the system. This page should include a number of "widgets" or "components". These include the following:
- Login name with login status
- A visual representation of at least 5 featured images, with 1 image receiving the main focus
- Links to all of the image categories
- Links to user functionality such as "upload image(s)", "settings" and "Sign out"
- A visual representation of most used "tags" on the site - this could be a tag cloud, or something more in line with the lumen concepts
- A visual representation of recently viewed assets
- Space for our companies logo (not yet designed so a placeholder should be used) - this shoudlnt' be the main focus and should be small (maybe in the footer)
- Space for our clients logo (this should be the primary logo on the page, maybe appearing in the top left hand corner)
2. The view asset page
- For the purposes of the design, assume that an asset is an uploaded image
- This page should use the same chrome as the homepage (chrome = common website components such as logo, navigation and login status)
- The asset/image should take up the majority of the screen size, which will be dynamically resizable
- to the right of the image there should be a metadata "bar" of information that will include metadata about the image such as author, uploaded date, file type, file size etc.)
- the metadata "bar" should be expandable/collapsible based on what the users wants to see - this should be reflect in the design
- underneath the image there should be several actions that a user can complete against the image. It is up to you how these are conveyed, but we think that an icon and label for each is probably a good bet, but we're open to suggestions. The actions are as follow:
- download image (this will have a drop down menu so this should be indicated, maybe with an arrow pointing downwards?)
- edit image
- rate image (maybe shown as a rating control?)
- add tag to image
- add comment to image
3. The view category page
- This page displays all of the assets/images in a given category
- We really like the concept shown here http://blogs.devnotes.example/b/q8/archive/2012/06/26/introducing-the-gallery-app-for-quillon-8.aspx (2nd picture down)
- users should be able to change the size of the images on the page (and thus changing the number of images displayed)
- a paging mechanism needs to be designed that will allow the user to page between screens - in an ideal world we would have similar paging to an tabro app (eg small dots that represent each page with the current page being slightly brighter). This removes the need for "page numbers". To be clear we don't like the "scroll horizontally to page" functioanlity that is common in the lumen UI
- please feel free to add your own twist on this page
The above 3 pages are REQUIRED for every design, but you may submit additional pages if you think they will benefit your design (for example settings pages, other UI elements, login pages, etc.)
If required please also submit a textual description of the functionality found on each page - for example if something is not clear from the flat design images.
The target users of this application will be marketing teams, website designers, graphic designers and press
Marketing

```html
<!DOCTYPE html>
<html lang="en">
<head>
<meta charset="utf-8">
<title>Asset Library – Home</title>
<link rel="stylesheet" href="https://fonts.googleapis.com/css2?family=Open+Sans:wght@300;400;600&display=swap">
<style>
  :root {
    --page-bg: #ececec;
    --ink: #333333;
    --ink-strong: #2a2a2a;
    --ink-muted: #9a9a9a;
    --rule: #cfcfcf;
    --accent: #d0104a;
    --accent-link: #e0224f;
    --caption-bg: rgba(10, 10, 10, 0.86);
    --white: #ffffff;
  }
  * { box-sizing: border-box; margin: 0; padding: 0; }
  html, body { width: 1200px; height: 769px; overflow: hidden; }
  body {
    position: relative;
    background: radial-gradient(ellipse at 60% 45%, #e4e4e4 0%, var(--page-bg) 60%);
    font-family: "Open Sans", sans-serif;
    color: var(--ink);
  }
  .abs { position: absolute; }
  a { color: inherit; text-decoration: none; }

  /* Header */
  .client-logo { left: 116px; top: 13px; font-size: 28px; font-weight: 400; color: var(--ink-strong); }
  .main-nav-item { top: 21px; display: flex; align-items: center; gap: 10px; font-size: 16px; color: var(--ink); height: 24px; }
  .main-nav-item svg { fill: var(--ink-strong); }
  .rule-h { height: 1px; background: var(--rule); }
  .rule-v { width: 1px; background: var(--rule); }

  /* Section headings */
  .section-title { font-size: 24px; font-weight: 400; color: var(--ink-strong); white-space: nowrap; }
  .section-link { font-size: 24px; font-weight: 400; color: var(--ink-muted); white-space: nowrap; }
  .greeting { left: 926px; top: 91px; display: flex; align-items: center; gap: 10px; font-size: 18px; color: var(--ink); }

  /* Featured images */
  .featured-main {
    left: 120px; top: 142px; width: 667px; height: 275px;
    background: linear-gradient(120deg, #b8481a 0%, #8a3212 30%, #3b2a1a 45%, #6f8a1e 62%, #2c2a12 78%, #a94617 100%);
  }
  .featured-caption {
    left: 120px; top: 356px; width: 667px; height: 61px; background: var(--caption-bg);
    color: var(--white); font-size: 12.5px; line-height: 21px;
  }
  .featured-caption .star { position: absolute; left: 16px; top: 15px; }
  .featured-caption .divider { position: absolute; left: 63px; top: 8px; bottom: 8px; width: 1px; background: rgba(255,255,255,0.25); }
  .featured-caption .meta { position: absolute; left: 74px; top: 9px; }
  .featured-caption .more { color: var(--accent-link); }
  .thumb { position: absolute; }

  /* Tags */
  .tag {
    position: absolute; width: 100px; height: 51px; background: var(--accent);
    color: var(--white); font-size: 21px; display: flex; align-items: center; justify-content: center;
    text-shadow: 0 1px 2px rgba(0,0,0,0.3);
  }

  /* Footer */
  .footer-link { top: 670px; font-size: 13px; color: var(--ink); }
  .footer-sep { top: 670px; font-size: 13px; color: var(--ink); }
  .powered-by { left: 850px; top: 670px; font-size: 13px; color: var(--ink); }
  .company-logo { left: 936px; top: 662px; font-size: 22px; color: var(--ink-strong); }
</style>
</head>
<body>

<header>
  <div class="abs client-logo">Client logo</div>
  <nav>
    <a class="abs main-nav-item" style="left:550px" href="#">
      <svg width="24" height="24" viewBox="0 0 24 24"><circle cx="12" cy="12" r="12"/><path d="M10.5 6h3v4.5H18v3h-4.5V18h-3v-4.5H6v-3h4.5z" fill="#ececec"/></svg>
      Upload
    </a>
    <a class="abs main-nav-item" style="left:686px" href="#">
      <svg width="24" height="24" viewBox="0 0 24 24"><path d="M13 1h10v10L11 23 1 13z"/><circle cx="18.5" cy="5.5" r="2" fill="#ececec"/></svg>
      Categories
    </a>
    <a class="abs main-nav-item" style="left:841px; gap:6px" href="#">
      <svg width="24" height="24" viewBox="0 0 24 24">
        <circle cx="8" cy="9" r="6"/><circle cx="8" cy="9" r="2.2" fill="#ececec"/>
        <g stroke="#2a2a2a" stroke-width="2.6"><path d="M8 1v16M0 9h16M2.3 3.3l11.4 11.4M13.7 3.3 2.3 14.7"/></g>
        <circle cx="8" cy="9" r="2.2" fill="#ececec"/>
        <circle cx="17.5" cy="18" r="4"/><g stroke="#2a2a2a" stroke-width="2"><path d="M17.5 12.5v11M12 18h11M13.6 14.1l7.8 7.8M21.4 14.1l-7.8 7.8"/></g>
        <circle cx="17.5" cy="18" r="1.5" fill="#ececec"/>
      </svg>
      Settings
    </a>
    <a class="abs main-nav-item" style="left:988px" href="#">
      <svg width="14" height="14" viewBox="0 0 14 14"><path d="M2 2l10 10M12 2 2 12" stroke="#2a2a2a" stroke-width="3"/></svg>
      Sign out
    </a>
  </nav>
</header>

<div class="abs rule-h" style="left:118px; top:67px; width:959px"></div>

<section class="featured">
  <div class="abs section-title" style="left:119px; top:88px">Your images</div>
  <div class="abs rule-v" style="left:267px; top:80px; height:47px"></div>
  <a class="abs section-link" style="left:287px; top:88px" href="#">Next 5</a>
  <div class="abs rule-v" style="left:375px; top:80px; height:47px"></div>
  <a class="abs section-link" style="left:395px; top:88px" href="#">All</a>
  <div class="abs rule-v" style="left:441px; top:80px; height:47px"></div>
  <a class="abs section-link" style="left:463px; top:88px" href="#">Share</a>

  <div class="abs greeting">
    <svg width="22" height="22" viewBox="0 0 22 22" fill="#333"><circle cx="11" cy="6" r="5.5"/><path d="M0 22c0-6 4-9.5 11-9.5S22 16 22 22z"/></svg>
    Hello Michael
  </div>

  <div class="abs featured-main" role="img" aria-label="Featured image: a tablet on a wooden table showing a glowing hexagon puzzle game"></div>
  <div class="abs featured-caption">
    <svg class="star" width="30" height="29" viewBox="0 0 24 23"><path d="M12 0l3.6 7.6 8.4 1-6.2 5.8 1.6 8.3L12 18.6 4.6 22.7l1.6-8.3L0 8.6l8.4-1z" fill="#fff"/></svg>
    <div class="divider"></div>
    <div class="meta">
      Categories: Design studio, Photo Shoot, Work in Progress<br>
      Tags: Design, people, white background, furniture, team, design company, <span class="more">and two more...</span>
    </div>
  </div>

  <div class="thumb" style="left:805px; top:142px; width:129px; height:128px; background:linear-gradient(160deg,#1a2330,#3a2640 45%,#e07ab0 60%,#1a2330)" role="img" aria-label="Fashion model in a patterned dress against a dark background"></div>
  <div class="thumb" style="left:951px; top:142px; width:127px; height:128px; background:linear-gradient(135deg,#ffffff 10%,#e8c23a 35%,#c83a2a 50%,#4a6fb0 65%,#ffffff 85%)" role="img" aria-label="Geometric poster with coloured diamond shapes on white"></div>
  <div class="thumb" style="left:805px; top:290px; width:129px; height:127px; background:linear-gradient(180deg,#d8dcdc 0%,#f2f2f2 55%,#c7c9c9 100%)" role="img" aria-label="Pots of pencils and plants on a window sill"></div>
  <div class="thumb" style="left:953px; top:290px; width:127px; height:127px; background:linear-gradient(180deg,#f1efec 0%,#e3ddd4 55%,#c9a877 100%)" role="img" aria-label="Modern lounge chair with cushions on a wooden frame"></div>
</section>

<div class="abs rule-h" style="left:120px; top:437px; width:960px"></div>
<div class="abs rule-v" style="left:599px; top:450px; height:175px"></div>

<section class="popular-tags">
  <div class="abs section-title" style="left:119px; top:459px">Most popular tags</div>
  <div class="abs rule-v" style="left:328px; top:451px; height:47px"></div>
  <a class="abs section-link" style="left:344px; top:459px" href="#">All</a>

  <a class="tag" style="left:120px; top:513px" href="#">Design</a>
  <a class="tag" style="left:232px; top:513px" href="#">Lumen</a>
  <a class="tag" style="left:344px; top:513px" href="#">UX</a>
  <a class="tag" style="left:455px; top:513px" href="#">Team</a>
  <a class="tag" style="left:120px; top:575px" href="#">Visual</a>
  <a class="tag" style="left:232px; top:575px" href="#">Mobile</a>
  <a class="tag" style="left:344px; top:575px" href="#">Arts</a>
  <a class="tag" style="left:455px; top:575px" href="#">Web</a>
</section>

<section class="recently-viewed">
  <div class="abs section-title" style="left:641px; top:457px">Recently viewed</div>
  <div class="abs rule-v" style="left:828px; top:450px; height:47px"></div>
  <a class="abs section-link" style="left:848px; top:457px" href="#">All</a>

  <div class="thumb" style="left:642px; top:512px; width:100px; height:50px; background:linear-gradient(120deg,#3a3a3a,#d8c23a 35%,#d23a6a 55%,#3aa0d0 75%,#2a2a2a)" role="img" aria-label="Colourful toy figures"></div>
  <div class="thumb" style="left:755px; top:512px; width:100px; height:50px; background:linear-gradient(160deg,#2a7ac8,#e07a2a 45%,#3a9ad8 70%,#1a4a90)" role="img" aria-label="Colourful 3D lettering artwork"></div>
  <div class="thumb" style="left:867px; top:512px; width:100px; height:50px; background:linear-gradient(180deg,#ffffff 40%,#e8e8e8 70%,#e07a2a 90%)" role="img" aria-label="Goldfish bowl on white"></div>
  <div class="thumb" style="left:979px; top:512px; width:100px; height:50px; background:linear-gradient(120deg,#3a3a3a,#d8c23a 35%,#d23a6a 55%,#3aa0d0 75%,#2a2a2a)" role="img" aria-label="Colourful toy figures"></div>
  <div class="thumb" style="left:642px; top:574px; width:100px; height:51px; background:linear-gradient(100deg,#e8dfc0,#7ac83a 45%,#4aa02a 70%,#d84a3a)" role="img" aria-label="Green cartoon chameleon illustration"></div>
  <div class="thumb" style="left:755px; top:574px; width:100px; height:51px; background:linear-gradient(135deg,#e83a3a,#f0a02a 30%,#e8e03a 50%,#3ab04a 65%,#3a7ad8 80%,#8a3ad0)" role="img" aria-label="Fanned colour swatch cards"></div>
  <div class="thumb" style="left:867px; top:574px; width:100px; height:51px; background:linear-gradient(90deg,#d83aa0,#f0e05a 30%,#a03ad8 60%,#e05ab0 85%)" role="img" aria-label="Bright neon packaging designs"></div>
  <div class="thumb" style="left:979px; top:574px; width:100px; height:51px; background:linear-gradient(160deg,#2a7ac8,#e07a2a 45%,#3a9ad8 70%,#1a4a90)" role="img" aria-label="Colourful 3D lettering artwork"></div>
</section>

<div class="abs rule-h" style="left:120px; top:650px; width:960px"></div>

<footer>
  <a class="abs footer-link" style="left:124px" href="#">Disclaimer</a>
  <span class="abs footer-sep" style="left:206px">|</span>
  <a class="abs footer-link" style="left:229px" href="#">Privacy Policy</a>
  <span class="abs footer-sep" style="left:327px">|</span>
  <a class="abs footer-link" style="left:349px" href="#">Terms</a>
  <span class="abs footer-sep" style="left:404px">|</span>
  <a class="abs footer-link" style="left:430px" href="#">Help</a>
  <span class="abs footer-sep" style="left:482px">|</span>
  <a class="abs footer-link" style="left:505px" href="#">Contact</a>

  <span class="abs powered-by">Powered by:</span>
  <span class="abs company-logo">Company logo</span>
</footer>

</body>
</html>
```